Tallow Creek Architectural Systems Business Card

We have a logo - but we need a business card. We are a specialty manufacturer of wood wall and ceiling panels. Please visit our website - www.tallowcreekas.com to see examples of our products.
We create wood architectural systems - so we would love to see wood on the card somehow. Maybe something similar to our grille system?
We would like a spot on the business card for a QR code that people can scan to add the contact to their phone (we have the QR codes - just need a spot on the card).
As for the contact info - we want to keep it simple. (Name, Cell phone, Fax, email, website)

Target Market(s)

Architects and general contractors

Industry/Entity Type

Construction

Contact Information for Business Card

Name, Cell phone, fax, email, website

Requirements
Must have
• space for a QR code, wood feature
Nice to have
• We just want something a little different - but not too crazy. We want to stand out - but in a professional way.
Should not have
• nothing too busy

```html
<!DOCTYPE html>
<html lang="en">
<head>
<meta charset="utf-8">
<title>Tallow Creek Architectural Systems – Business Card</title>
<link href="https://fonts.googleapis.com/css2?family=Saira:wght@500;700&family=Saira+Condensed:wght@600&display=swap" rel="stylesheet">
<style>
  :root {
    --backdrop: #9b9b9b;
    --brand-red: #b01e25;
    --card-dark: #272727;
    --ink-light: #ffffff;
    --wood-light: #c38d5a;
    --wood-mid: #a8723f;
    --wood-dark: #7e5029;
    --slat-gap: #5a1014;
  }
  * { margin: 0; padding: 0; box-sizing: border-box; }
  html, body {
    width: 1133px;
    height: 1200px;
    overflow: hidden;
    background: var(--backdrop);
  }
  .canvas { position: relative; width: 1133px; height: 1200px; }
  .card { position: absolute; border-radius: 19px; overflow: hidden; }
  .card--front {
    left: 197px; top: 144px; width: 724px; height: 412px;
    background: var(--brand-red);
  }
  .card--back {
    left: 200px; top: 640px; width: 719px; height: 410px;
    background: var(--card-dark);
    display: flex; align-items: center; justify-content: center; gap: 20px;
  }

  /* wood grille feature */
  .wood-grille {
    position: absolute;
    left: 0; top: 0;
    width: 410px; height: 412px;
    background:
      linear-gradient(180deg, rgba(255,255,255,0.08), rgba(0,0,0,0.18)),
      repeating-linear-gradient(90deg,
        var(--wood-light) 0 6px,
        var(--wood-mid) 6px 16px,
        var(--wood-dark) 16px 22px,
        var(--slat-gap) 22px 32px);
  }
  .qr-space {
    position: absolute;
    left: 294px; bottom: 34px;
    width: 96px; height: 96px;
    background: var(--ink-light);
    border-radius: 6px;
  }

  .company-name {
    font-family: "Saira", sans-serif;
    font-weight: 700;
    color: var(--ink-light);
    text-transform: uppercase;
    line-height: 1.1;
  }
  .company-name__main { display: block; font-size: 29px; letter-spacing: 0.02em; }
  .company-name__sub  { display: block; font-size: 14.5px; letter-spacing: 0.16em; margin-top: 3px; }
  .card--front .company-name { position: absolute; left: 451px; top: 54px; }
  .card--back .company-name .company-name__main { font-size: 38px; }
  .card--back .company-name .company-name__sub { font-size: 19px; }
  .brand-square { width: 84px; height: 84px; background: var(--brand-red); }

  .contact {
    position: absolute; left: 451px; top: 180px;
    color: var(--ink-light);
    font-family: "Saira", sans-serif; font-weight: 500;
  }
  .contact__name {
    font-family: "Saira Condensed", sans-serif; font-weight: 600;
    font-size: 29px; line-height: 1; text-transform: uppercase;
  }
  .contact__title { font-size: 16px; line-height: 1.3; margin-top: 2px; }
  .contact__address { margin-top: 16px; font-size: 16px; line-height: 1.25; }
  .contact__list { list-style: none; margin-top: 8px; font-size: 16px; line-height: 1.3; }
  .contact__list li { display: flex; align-items: center; gap: 8px; }
  .contact__list svg { width: 14px; height: 14px; flex: none; fill: var(--ink-light); }
</style>
</head>
<body>
<main class="canvas">
  <section class="card card--front">
    <div class="wood-grille" role="img" aria-label="Vertical wood slat grille panel"></div>
    <div class="qr-space" role="img" aria-label="Space for contact QR code"></div>

    <div class="company-name">
      <span class="company-name__main">Tallow Creek</span>
      <span class="company-name__sub">Architectural Systems</span>
    </div>

    <div class="contact">
      <div class="contact__name">Daniel Mercer</div>
      <div class="contact__title">Founder &amp; CEO</div>
      <div class="contact__address">4820 West Harlan Ave<br>Tulsa, Oklahoma 74120</div>
      <ul class="contact__list">
        <li>
          <svg viewBox="0 0 16 16" aria-hidden="true"><path d="M3.6 1.2l2.3 2.6-1.3 1.9c.9 2 2.6 3.7 4.6 4.6l1.9-1.3 2.6 2.3-1.5 2.5C7 13.5 2.5 9 1.2 3.1z"/></svg>
          Cell 918-555-0172
        </li>
        <li>
          <svg viewBox="0 0 16 16" aria-hidden="true"><path d="M4 1h6l2 2v3H4z M1 7h14v7H1z M3 9v1h2V9z" fill-rule="evenodd"/></svg>
          Fax 918-555-0173
        </li>
        <li>
          <svg viewBox="0 0 16 16" aria-hidden="true"><path d="M1 3.5h14v9H1z M2.2 4.5 8 8.6l5.8-4.1v-.1H2.2z" fill-rule="evenodd"/></svg>
          sales@tallowcreekas.com
        </li>
        <li>
          <svg viewBox="0 0 16 16" aria-hidden="true"><path d="M8 1a7 7 0 1 0 0 14A7 7 0 0 0 8 1zm0 1.5c.9 0 1.9 1.9 2.1 4.7H5.9C6.1 4.4 7.1 2.5 8 2.5zM2.6 8.8h1.8c.1 1.6.4 2.9.9 3.9a5.5 5.5 0 0 1-2.7-3.9zm0-1.6a5.5 5.5 0 0 1 2.7-3.9c-.5 1-.8 2.3-.9 3.9zm3.3 1.6h4.2c-.2 2.8-1.2 4.7-2.1 4.7S6.1 11.6 5.9 8.8zm5.7 0h1.8a5.5 5.5 0 0 1-2.7 3.9c.5-1 .8-2.3.9-3.9zm0-1.6c-.1-1.6-.4-2.9-.9-3.9a5.5 5.5 0 0 1 2.7 3.9z"/></svg>
          www.tallowcreekas.com
        </li>
      </ul>
    </div>
  </section>

  <section class="card card--back">
    <div class="brand-square"></div>
    <div class="company-name">
      <span class="company-name__main">Tallow Creek</span>
      <span class="company-name__sub">Architectural Systems</span>
    </div>
  </section>
</main>
</body>
</html>
```